New modern business card design

To design a brand new business card that's clean & modern in terms of layout.
I have attached our company logo and also basic information regarding what is needed on the card that also needs to be editable.

Target Market(s)

motor trade

Contact Information for Business Card

logo, name, title, tel, mob, email, address, www, all information is in the word.doc file

Requirements
Must have
• white background
Nice to have
• Nice clean font

```html
<!DOCTYPE html>
<html lang="en">
<head>
<meta charset="utf-8">
<title>Bolt Draw Ltd – Business Card</title>
<link rel="stylesheet" href="https://fonts.googleapis.com/css2?family=Montserrat:wght@400;500;600;700&display=swap">
<style>
  :root {
    --page-bg: #ececec;
    --card-white: #f7f7f7;
    --card-dark: #2b2b2b;
    --brand-blue: #2a7bc0;
    --text-dark: #3a3a3a;
    --text-mid: #555555;
    --rule: #bdbdbd;
    --back-text: #d8d8d8;
  }
  * { margin: 0; padding: 0; box-sizing: border-box; }
  html, body {
    width: 1200px; height: 1158px; overflow: hidden;
    background: var(--page-bg);
    font-family: "Montserrat", Arial, sans-serif;
  }
  .card {
    position: absolute; left: 150px;
    width: 900px; height: 520px;
    box-shadow: 0 6px 18px rgba(0,0,0,0.12);
  }
  .card--front { top: 40px; background: var(--card-white); }
  .card--back { top: 598px; background: var(--card-dark); }

  .brand {
    display: flex; align-items: center; justify-content: center;
    color: var(--brand-blue);
    font-weight: 600;
    white-space: nowrap;
  }
  .brand__mark { background: var(--brand-blue); flex: none; }

  .card--front .brand {
    position: absolute; left: 30px; width: 410px; top: 236px;
    font-size: 30px; letter-spacing: 1px; gap: 12px;
  }
  .card--front .brand__mark { width: 24px; height: 24px; }

  .divider {
    position: absolute; left: 470px; top: 110px;
    width: 1px; height: 300px; background: var(--rule);
  }
  .contact { position: absolute; left: 515px; top: 130px; color: var(--text-mid); }
  .contact__name { font-weight: 700; font-size: 32px; color: var(--text-dark); }
  .contact__title { font-size: 18px; margin-top: 4px; }
  .contact__address { font-size: 18px; line-height: 26px; margin-top: 22px; }
  .contact__list { list-style: none; margin-top: 20px; font-size: 18px; line-height: 30px; }
  .contact__list li { display: flex; align-items: center; gap: 12px; }
  .contact__list svg { width: 18px; height: 18px; flex: none; }

  .card--back .brand {
    position: absolute; left: 0; right: 0; top: 215px;
    font-size: 40px; letter-spacing: 2px; gap: 14px;
  }
  .card--back .brand__mark { width: 30px; height: 30px; }
  .back__web {
    position: absolute; left: 0; right: 0; top: 300px;
    text-align: center; color: var(--back-text);
    font-size: 18px; letter-spacing: 2px;
  }
</style>
</head>
<body>
  <section class="card card--front" aria-label="Business card front">
    <div class="brand"><span class="brand__mark"></span>BOLT DRAW LTD</div>
    <div class="divider"></div>
    <div class="contact">
      <p class="contact__name">Daniel Hartley</p>
      <p class="contact__title">General Manager</p>
      <p class="contact__address">Carlton Road, Denton<br>Manchester, M34 7QP</p>
      <ul class="contact__list">
        <li>
          <svg viewBox="0 0 24 24" fill="none" stroke="#2a7bc0" stroke-width="2"><path d="M5 3h4l2 5-3 2a11 11 0 0 0 6 6l2-3 5 2v4a2 2 0 0 1-2 2A17 17 0 0 1 3 5a2 2 0 0 1 2-2z"/></svg>
          0161 555 0192
        </li>
        <li>
          <svg viewBox="0 0 24 24" fill="none" stroke="#2a7bc0" stroke-width="2"><rect x="6" y="2" width="12" height="20" rx="2"/><line x1="11" y1="18" x2="13" y2="18"/></svg>
          07700 900 418
        </li>
        <li>
          <svg viewBox="0 0 24 24" fill="none" stroke="#2a7bc0" stroke-width="2"><rect x="2" y="5" width="20" height="14"/><path d="M2 5l10 8 10-8"/></svg>
          dhartley@boltdraw.co.uk
        </li>
        <li>
          <svg viewBox="0 0 24 24" fill="none" stroke="#2a7bc0" stroke-width="2"><circle cx="12" cy="12" r="10"/><path d="M2 12h20M12 2c3 3 3 17 0 20M12 2c-3 3-3 17 0 20"/></svg>
          www.boltdraw.co.uk
        </li>
      </ul>
    </div>
  </section>

  <section class="card card--back" aria-label="Business card back">
    <div class="brand"><span class="brand__mark"></span>BOLT DRAW LTD</div>
    <p class="back__web">www.boltdraw.co.uk</p>
  </section>
</body>
</html>
```